Window cleaning company in need of leaflet design

Family run business requires leaflet design.
Our company uses water fed pole with pure water which is what the leaflet needs to emphasise on (include a background picture of a water fed pole cleaning a window.)

other services we offer which i would like to include are:
• facia/soffit cleaning.
• Conservatory cleans.
• Gutter clearing which is performed by a gutter vacuum pictures of gutters before and after clean are provided to every customer if they require.
• pressure washing

uploaded company logo to be included on leaflet.
number to include is 07942615380
email address is Tbglasswash@mailvento.com
would also like a facebook symbol included to show we are on social media.
Thank you

Font styles to use
Serif
Sans Serif

Colors
00a990
33a6d7
3276b5
3277b5
34a7d8
87cfc6
33b8a4
cfdfed
85acd3

Requirements
Must have
• We use traditional and water fed pole methods of cleaning. So those hard to reach or awkward to clean windows are not a problem. No need for ladders.

Our water fed pole system uses 100% pure water. This is water that has been de-ironised and de-mineralised to ensue it’s perfectly pure for a spot free finish.

• fully insured

• regular and reliable service
• one off cleans available

Call dean on 07942615380 for a free quote

```html
<!DOCTYPE html>
<html lang="en">
<head>
<meta charset="utf-8">
<title>T.B Glass Wash leaflet</title>
<link href="https://fonts.googleapis.com/css2?family=Barlow:wght@400;500;600;700&family=Barlow+Condensed:wght@600;700&display=swap" rel="stylesheet">
<style>
  :root {
    --navy: #2e3379;
    --navy-deep: #262a66;
    --charcoal: #3a3a3d;
    --body-grey: #555558;
    --white: #ffffff;
    --teal-dark: #1f3a3a;
  }
  * { margin: 0; padding: 0; box-sizing: border-box; }
  html, body { width: 970px; height: 1200px; overflow: hidden; background: var(--white); }
  body { font-family: 'Barlow', sans-serif; position: relative; }

  .leaflet { position: relative; width: 970px; height: 1200px; background: var(--white); overflow: hidden; }

  .top-rule { position: absolute; left: 0; top: 189px; width: 892px; height: 5px; background: var(--navy); }

  .hero {
    position: absolute; left: 0; top: 193px; width: 892px; height: 566px;
    border-bottom-right-radius: 62px; overflow: hidden;
  }
  .hero-photo {
    position: absolute; inset: 0 0 187px 0;
    background: linear-gradient(160deg, #c9c4c2 0%, #9a6e5c 35%, #8a5b48 55%, #3d4b40 80%, #5d7a3e 100%);
  }
  .headline-band {
    position: absolute; left: 0; top: 379px; width: 892px; height: 84px;
    background: var(--navy); border-top-right-radius: 44px;
  }
  .headline {
    position: absolute; left: 47px; top: 10px;
    font-family: 'Barlow Condensed', sans-serif; font-weight: 700;
    font-size: 56px; letter-spacing: 0.5px; color: var(--white); line-height: 1.15;
  }
  .services-band {
    position: absolute; left: 0; top: 463px; width: 892px; height: 103px;
    background: linear-gradient(90deg, #2a3a3a 0%, #1f3434 45%, #2a3550 75%, #262c5c 100%);
  }
  .services { position: absolute; left: 47px; top: 14px; display: flex; gap: 0; list-style: none; }
  .service { display: flex; align-items: flex-start; color: var(--white); font-weight: 600; font-size: 27px; line-height: 1.3; }
  .service svg { margin-top: 6px; margin-right: 10px; flex: none; }
  .service:nth-child(1) { width: 214px; }
  .service:nth-child(2) { width: 228px; }
  .service:nth-child(3) { width: 158px; }

  .wash-photo {
    position: absolute; left: 40px; top: 0; width: 252px; height: 307px;
    border: 4px solid var(--navy); border-top: none; border-left: none;
    border-bottom-right-radius: 52px; overflow: hidden;
    background: linear-gradient(135deg, #a08f7e 0%, #8d7c6b 40%, #d8d2c8 55%, #6f6152 100%);
  }

  .brand { position: absolute; left: 430px; top: 112px; width: 462px; text-align: right; }
  .brand-name { font-family: 'Barlow', sans-serif; font-weight: 500; font-size: 52px; color: var(--navy); letter-spacing: 0.5px; }

  .intro { position: absolute; left: 47px; top: 782px; width: 540px; color: var(--body-grey); font-size: 17.5px; line-height: 1.33; }
  .intro p + p { margin-top: 16px; }

  .assurances {
    position: absolute; left: 0; top: 938px; width: 600px; height: 68px;
    background: var(--navy); display: flex; align-items: center; padding-left: 47px;
  }
  .assurance { display: flex; align-items: center; color: var(--white); font-weight: 600; font-size: 18px; line-height: 1.28; text-transform: uppercase; }
  .assurance svg { margin-right: 7px; flex: none; }
  .assurance:nth-child(1) { width: 123px; }
  .assurance:nth-child(2) { width: 212px; }

  .gutter-compare {
    position: absolute; left: 581px; top: 777px; width: 311px; height: 241px;
    border: 3px solid var(--navy); border-radius: 26px; overflow: hidden;
    background: linear-gradient(90deg, #e4e6ea 0%, #c5c9c8 30%, #6f7d4f 45%, #cfd6e4 55%, #b7c3da 80%, #8b8d8a 100%);
  }
  .tab {
    position: absolute; background: var(--navy); color: var(--white);
    font-family: 'Barlow Condensed', sans-serif; font-weight: 600; font-size: 15px; padding: 3px 10px;
  }
  .tab-before { left: 0; top: 0; border-bottom-right-radius: 12px; }
  .tab-after { right: 0; top: 0; border-bottom-left-radius: 12px; }
  .tab-method { left: 50%; bottom: 0; transform: translateX(-50%); border-radius: 12px 12px 0 0; padding: 3px 20px; }

  .call { position: absolute; left: 47px; top: 1028px; width: 845px; display: flex; align-items: center; }
  .call-lead { font-weight: 600; font-size: 31px; line-height: 1.05; color: var(--charcoal); text-align: right; text-transform: uppercase; }
  .call-lead .name { color: var(--navy); }
  .call-number { font-weight: 600; font-size: 86px; line-height: 1; color: var(--navy); margin: 0 6px 0 12px; letter-spacing: -1px; }
  .call-tail { font-weight: 600; font-size: 31px; line-height: 1.05; color: var(--charcoal); text-align: center; text-transform: uppercase; }

  .footer-bar { position: absolute; left: 0; top: 1131px; width: 970px; height: 69px; }
  .footer-bar svg { position: absolute; inset: 0; }
  .social { position: absolute; left: 40px; top: 1121px; width: 78px; text-align: center; color: var(--white); }
  .social-dot { width: 46px; height: 46px; border-radius: 50%; border: 3px solid var(--navy); background: var(--white); margin: 0 auto; }
  .social-label { font-weight: 600; font-size: 13px; margin-top: 5px; }
  .contact-line { position: absolute; left: 198px; top: 1143px; color: var(--white); font-weight: 600; font-size: 33px; letter-spacing: 0.2px; }
</style>
</head>
<body>
<main class="leaflet">
  <div class="top-rule"></div>

  <section class="hero">
    <div class="hero-photo" role="img" aria-label="Photo of a worker using a water fed pole to clean windows on a brick block of flats"></div>
    <div class="headline-band">
      <h1 class="headline">WATER FED POLE WITH PURE WATER</h1>
    </div>
    <div class="services-band" role="img" aria-label="Darkened photo of water fed pole equipment behind the service list">
      <ul class="services">
        <li class="service"><svg width="30" height="26" viewBox="0 0 30 26"><polyline points="3,14 11,22 27,3" fill="none" stroke="#fff" stroke-width="5"/></svg><span>Facia/Soffit<br>Cleaning</span></li>
        <li class="service"><svg width="30" height="26" viewBox="0 0 30 26"><polyline points="3,14 11,22 27,3" fill="none" stroke="#fff" stroke-width="5"/></svg><span>Conservatory<br>Cleans</span></li>
        <li class="service"><svg width="30" height="26" viewBox="0 0 30 26"><polyline points="3,14 11,22 27,3" fill="none" stroke="#fff" stroke-width="5"/></svg><span>Gutter<br>Clearing</span></li>
        <li class="service"><svg width="30" height="26" viewBox="0 0 30 26"><polyline points="3,14 11,22 27,3" fill="none" stroke="#fff" stroke-width="5"/></svg><span>Pressure<br>Washing</span></li>
      </ul>
    </div>
  </section>

  <div class="wash-photo" role="img" aria-label="Close-up photo of a pressure washer lance cleaning block paving"></div>

  <header class="brand">
    <div class="brand-name">T.B Glass Wash</div>
  </header>

  <section class="intro">
    <p>We use traditional and water fed pole methods of cleaning. So those hard to reach or awkward to clean windows are not a problem. No need for ladders.</p>
    <p>Our water fed pole system uses 100% pure water. This is water that has been de-ironised and de-mineralised to ensue it’s perfectly pure for a spot free finish.</p>
  </section>

  <section class="assurances">
    <div class="assurance"><svg width="30" height="26" viewBox="0 0 30 26"><polyline points="3,14 11,22 27,3" fill="none" stroke="#fff" stroke-width="5"/></svg><span>Fully<br>Insured</span></div>
    <div class="assurance"><svg width="30" height="26" viewBox="0 0 30 26"><polyline points="3,14 11,22 27,3" fill="none" stroke="#fff" stroke-width="5"/></svg><span>Regular and<br>reliable service</span></div>
    <div class="assurance"><svg width="30" height="26" viewBox="0 0 30 26"><polyline points="3,14 11,22 27,3" fill="none" stroke="#fff" stroke-width="5"/></svg><span>One off cleans<br>available</span></div>
  </section>

  <figure class="gutter-compare" role="img" aria-label="Before and after photos of a roof gutter cleared with a gutter vacuum">
    <span class="tab tab-before">BEFORE</span>
    <span class="tab tab-after">AFTER</span>
    <span class="tab tab-method">GUTTER VACUUM</span>
  </figure>

  <section class="call">
    <div class="call-lead">Call<br><span class="name">Dean</span> on</div>
    <div class="call-number">07942615380</div>
    <div class="call-tail">For a<br>free quote</div>
  </section>

  <footer>
    <div class="footer-bar">
      <svg width="970" height="69" viewBox="0 0 970 69">
        <polygon points="133,0 970,0 970,69 165,69" fill="#3a3a3d"/>
        <polygon points="0,20 140,20 165,69 0,69" fill="#2e3379"/>
      </svg>
    </div>
    <div class="social">
      <div class="social-dot"></div>
      <div class="social-label">FOLLOW US</div>
    </div>
    <div class="contact-line">07942615380 | Tbglasswash@mailvento.com</div>
  </footer>
</main>
</body>
</html>
```